Kestrova Physical Therapy Website

I would need a clean modern website built to showcase my Physical therapy brand and services. I would need a simple but descriptive website that can ultimately connect my patients to my electronic medical portal so they may book an appointment..

```html
<!DOCTYPE html>
<html lang="en">
<head>
<meta charset="utf-8">
<title>Kestrova Physical Therapy</title>
<link href="https://fonts.googleapis.com/css2?family=Manrope:wght@400;500;600;700;800&family=Roboto:wght@400;500;700&display=swap" rel="stylesheet">
<style>
:root{
  --teal:#1b7a70;
  --teal-dark:#14695f;
  --green:#6cbf4a;
  --ink:#1d1d1d;
  --text:#3a3a3a;
  --soft:#f3f0f0;
  --blue:#3a4aa0;
  --footer:#262626;
  --line:#2f8f83;
}
*{box-sizing:border-box;margin:0;padding:0}
html,body{width:1200px;height:4098px;overflow:hidden;background:#fff}
body{position:relative;font-family:"Roboto",sans-serif;color:var(--text)}
.abs{position:absolute}
.btn{position:absolute;display:flex;align-items:center;justify-content:center;border-radius:6px;color:#fff;font-family:"Manrope",sans-serif;font-weight:800;letter-spacing:.5px}
.btn-green{background:var(--green)}
.btn-teal{background:var(--teal)}
/* header */
.brand{position:absolute;font-family:"Manrope",sans-serif;font-weight:800;color:var(--teal);font-size:30px;letter-spacing:1px}
.call{left:592px;top:22px;display:flex;align-items:center;gap:14px}
.call .lbl{font-size:13px;color:var(--ink)}
.call .num{font-size:24px;color:var(--ink)}
.call .sep{width:1px;height:44px;background:#999}
.nav{left:510px;top:100px;display:flex;gap:0}
.nav a{position:absolute;font-size:15px;color:var(--ink);text-decoration:none;white-space:nowrap}
.nav a.active{color:var(--green);text-decoration:underline;text-underline-offset:4px}
/* hero */
.hero{left:0;top:140px;width:1200px;height:548px;background:linear-gradient(100deg,#d9d9d6 0%,#eeeeec 40%,#f4f4f2 70%,#d6d8d4 100%)}
.hero-card{left:745px;top:220px;width:337px;height:307px;background:rgba(255,255,255,.85);border-radius:6px}
.hero-title{left:790px;top:266px;font-family:"Manrope",sans-serif;font-weight:800;font-size:47px;line-height:52px;color:var(--teal)}
.dots{left:562px;top:648px;display:flex;gap:9px}
.dots i{width:7px;height:7px;border-radius:50%;background:#222;display:block}
/* section headings */
.h2{position:absolute;left:0;width:1200px;text-align:center;font-family:"Manrope",sans-serif;font-weight:800;font-size:24px;color:var(--ink)}
/* services */
.svc{position:absolute;width:306px;height:245px;border-radius:8px;overflow:hidden}
.svc .ph{position:absolute;inset:0}
.svc .shade{position:absolute;inset:0;background:linear-gradient(to bottom,rgba(0,0,0,0) 45%,rgba(0,0,0,.72) 100%)}
.svc span{position:absolute;left:22px;bottom:20px;color:#fff;font-family:"Manrope",sans-serif;font-weight:700;font-size:16.5px;letter-spacing:.6px;line-height:21px}
/* welcome */
.welcome{left:0;top:1387px;width:1200px;height:422px;background:var(--soft);overflow:hidden}
.welcome-pre{left:128px;top:1425px;font-family:"Manrope",sans-serif;font-size:20px;color:var(--ink)}
.welcome-name{left:128px;top:1455px;font-family:"Manrope",sans-serif;font-weight:800;font-size:25px;color:var(--ink)}
.welcome-underline{left:128px;top:1489px;width:10px;height:0}
.copy{position:absolute;font-size:14.3px;line-height:22.4px;color:var(--text)}
.quote{left:815px;top:1470px;width:265px;color:#fff;font-size:17.5px;line-height:25.7px}
.qmark{font-family:"Manrope",sans-serif;font-weight:800;color:#fff;font-size:40px}
/* attention */
.area{position:absolute;width:223px;height:71px;border:1.5px solid #6fb3a7;border-radius:6px;display:flex;align-items:center;gap:14px;padding-left:10px;font-size:15px;color:var(--ink)}
.area .ico{width:54px;height:54px;border-radius:50%;background:radial-gradient(circle at 40% 40%,#e9414a 0 30%,#f3b6b9 31% 55%,#eaeef5 56%)}
/* find */
.find-photo{left:0;top:2333px;width:578px;height:485px;border-radius:0 60px 0 0;background:linear-gradient(110deg,#cfd8de 0%,#e9eef0 45%,#b8a596 70%,#dde3e6 100%)}
.find-bg{left:578px;top:2333px;width:622px;height:485px;background:var(--soft)}
/* stories */
.story{position:absolute;width:298px;height:385px;border-radius:10px;overflow:hidden;background:var(--blue)}
.story .ph{height:178px}
.story .body{text-align:center;color:#fff;padding:0 22px}
.story .q{font-family:"Manrope",sans-serif;font-weight:800;font-size:34px;line-height:34px;margin-top:8px}
.story h3{font-family:"Manrope",sans-serif;font-weight:800;font-size:13.5px;line-height:22px;letter-spacing:.3px;margin-top:6px}
.story p{font-size:12px;line-height:17.5px;margin-top:14px;color:#e3e6f5}
/* cta */
.cta{left:0;top:3420px;width:1200px;height:325px;background:linear-gradient(100deg,#8a8886 0%,#b4a79c 35%,#a49e9a 60%,#8c8a88 100%)}
/* footer */
.footer{left:0;top:3745px;width:1200px;height:353px;background:var(--footer);color:#fff}
.f-h{position:absolute;font-family:"Manrope",sans-serif;font-weight:800;font-size:13px;letter-spacing:.5px}
.f-menu{position:absolute;font-size:12px;line-height:25.5px;color:#e5e5e5}
.f-row{position:absolute;display:flex;align-items:center;gap:12px;font-size:11.5px;line-height:15px;color:#e5e5e5}
.f-row .c{width:24px;height:24px;border-radius:50%;background:#fff;flex:none;display:flex;align-items:center;justify-content:center}
</style>
</head>
<body>

<!-- header -->
<div class="brand" style="left:130px;top:86px;font-size:26px">KESTROVA</div>
<div class="abs" style="left:146px;top:28px;width:44px;height:44px;border-radius:50%;background:var(--teal)"></div>
<div class="abs call">
  <svg width="34" height="34" viewBox="0 0 24 24" fill="none" stroke="var(--teal)" stroke-width="1.6"><path d="M5 3h4l2 5-2.5 1.5a11 11 0 0 0 6 6L16 13l5 2v4a2 2 0 0 1-2 2A17 17 0 0 1 3 5a2 2 0 0 1 2-2z"/></svg>
  <div class="sep"></div>
  <div><div class="lbl">CALL US</div><div class="num">555.014.2290</div></div>
</div>
<div class="btn btn-teal" style="left:834px;top:24px;width:231px;height:50px;font-size:14.5px">BOOK AN APPOINTMENT</div>
<nav class="abs nav" style="left:0;top:100px">
  <a class="active" style="left:510px">HOME</a>
  <a style="left:601px">ABOUT US</a>
  <a style="left:730px">SERVICES</a>
  <a style="left:853px">PATIENTS</a>
  <a style="left:973px">CONTACT US</a>
</nav>

<!-- hero -->
<div class="abs hero" role="img" aria-label="Photo of a therapist guiding a woman through a resistance band exercise in a bright clinic"></div>
<div class="abs hero-card"></div>
<div class="abs hero-title">PHYSICAL<br>THERAPY<br>FOR LIFE</div>
<div class="btn btn-green" style="left:793px;top:440px;width:142px;height:45px;font-size:15.5px">READ MORE</div>
<div class="abs dots"><i></i><i></i><i></i><i></i><i></i></div>

<!-- services -->
<div class="h2" style="top:735px">OUR THERAPY SERVICES</div>
<div class="abs" style="left:577px;top:776px;width:46px;height:2px;background:var(--line)"></div>

<div class="svc" style="left:129px;top:822px"><div class="ph" role="img" aria-label="Patient exercising with a ball beside a therapist" style="background:linear-gradient(120deg,#c9b49a,#7d8ea6 60%,#3c4a63)"></div><div class="shade"></div><span>PHYSICAL THERAPY</span></div>
<div class="svc" style="left:446px;top:822px"><div class="ph" role="img" aria-label="Therapist assessing an older man's spine" style="background:linear-gradient(120deg,#dcdcdc,#a7a4a0 55%,#6d6a68)"></div><div class="shade"></div><span>SPINE PHYSICAL THERAPY</span></div>
<div class="svc" style="left:758px;top:822px"><div class="ph" role="img" aria-label="Therapist treating a patient's knee" style="background:linear-gradient(120deg,#7fa7b8,#c7a48c 55%,#3e3b3c)"></div><div class="shade"></div><span>ORTHOPEDIC<br>PHYSICAL THERAPY</span></div>
<div class="svc" style="left:129px;top:1079px"><div class="ph" role="img" aria-label="Athlete doing a leg exercise with a therapist" style="background:linear-gradient(120deg,#d3dbe0,#8e9aa6 50%,#3c3f46)"></div><div class="shade"></div><span>ATHLETIC PERFORMANCE</span></div>
<div class="svc" style="left:446px;top:1079px"><div class="ph" role="img" aria-label="Woman exercising on a stability ball" style="background:linear-gradient(120deg,#eeeeec,#b9b6b2 55%,#6c6a68)"></div><div class="shade"></div><span>OCCUPATIONAL THERAPY</span></div>
<div class="svc" style="left:758px;top:1079px"><div class="ph" role="img" aria-label="Hands massaging a patient's palm" style="background:linear-gradient(120deg,#f1f1ef,#d9a88c 55%,#59504b)"></div><div class="shade"></div><span>HAND THERAPY</span></div>

<!-- welcome -->
<div class="abs welcome">
  <svg class="abs" style="left:0;top:0" width="1200" height="422" viewBox="0 0 1200 422">
    <path d="M1200 0H640C700 30 760 110 740 210C725 300 690 370 655 422H1200Z" fill="var(--teal)"/>
  </svg>
  <div class="abs" role="img" aria-label="Emblem decoration" style="left:490px;top:40px;width:220px;height:220px;border-radius:50%;background:#fff"></div>
</div>
<div class="abs welcome-pre">Welcome to</div>
<div class="abs welcome-name">Kestrova Physical Therapy</div>
<div class="abs" style="left:128px;top:1488px;width:315px;height:1.5px;background:#444"></div>
<div class="copy" style="left:128px;top:1525px;width:330px">Lorem ipsum dolor sit amet, consectetur adipi scing elit, sed do eiusmod tempor incididunt ut labore et dolore magna aliqua. Ut enim ad minim veniam, quis nostrud exercitation ullamco laboris nisi ut aliquip ex ea commodo consequat. Duis aute irure dolor in repreh enderit in voluptate velit esse cillum dolore eu fugiat nulla pariatur.</div>
<div class="btn btn-green" style="left:128px;top:1729px;width:111px;height:35px;font-size:13px;border-radius:5px">READ MORE</div>
<div class="abs qmark" style="left:793px;top:1425px">&ldquo;</div>
<div class="abs quote">llamco laboris nisi ut aliquip ex ea commodo consequat. Duis aute irure dolor in repreh enderit in voluptate velit esse cillum dolore eu fugiat nulla pariatur. Excepteur sint occaecat cupidatat non proident, sunt in culpa qui officia deserunt.</div>
<div class="abs" role="img" aria-label="Patient portrait" style="left:815px;top:1713px;width:42px;height:42px;border-radius:50%;background:linear-gradient(135deg,#e8c9a8,#a07a5c)"></div>
<div class="abs" style="left:872px;top:1713px;color:#fff;font-size:17px">Daniel</div>
<div class="abs" style="left:872px;top:1737px;color:#e4f1ef;font-size:13px">England</div>

<!-- attention -->
<div class="h2" style="top:1868px">WHERE DO YOU NEED ATTENTION?</div>
<div class="abs" style="left:0;top:1910px;width:1200px;text-align:center;font-size:14.5px;color:var(--ink)">Choose the area of your injury or pain from the below options.</div>
<div class="abs" style="left:577px;top:1951px;width:46px;height:2px;background:var(--line)"></div>

<div class="area" style="left:129px;top:2001px"><div class="ico" role="img" aria-label="Head pain area"></div>HEAD</div>
<div class="area" style="left:368px;top:2001px"><div class="ico" role="img" aria-label="Neck pain area"></div>NECK</div>
<div class="area" style="left:606px;top:2001px"><div class="ico" role="img" aria-label="Shoulder pain area"></div>SHOULDER</div>
<div class="area" style="left:844px;top:2001px"><div class="ico" role="img" aria-label="Knee pain area"></div>KNEE</div>
<div class="area" style="left:129px;top:2098px"><div class="ico" role="img" aria-label="Hand pain area"></div>HAND</div>
<div class="area" style="left:368px;top:2098px"><div class="ico" role="img" aria-label="Back pain area"></div>BACK</div>
<div class="area" style="left:606px;top:2098px"><div class="ico" role="img" aria-label="Hip pain area"></div>HIP</div>
<div class="area" style="left:844px;top:2098px"><div class="ico" role="img" aria-label="Leg pain area"></div>LEG</div>
<div class="area" style="left:368px;top:2194px"><div class="ico" role="img" aria-label="Foot pain area"></div>FOOT</div>
<div class="area" style="left:606px;top:2194px"><div class="ico" role="img" aria-label="Ankle pain area"></div>ANKLE</div>

<!-- find a therapist -->
<div class="abs find-bg"></div>
<div class="abs find-photo" role="img" aria-label="Therapist helping a man lift light dumbbells in a bright room"></div>
<div class="abs" style="left:634px;top:2420px;font-family:'Manrope',sans-serif;font-weight:800;font-size:30px;color:var(--ink)">Find a Physical Therapist</div>
<div class="copy" style="left:634px;top:2486px;width:330px">Lorem ipsum dolor sit amet, consectetur adipi scing elit, sed do eiusmod tempor incididunt ut labore et dolore magna aliqua. Ut enim ad minim veniam, quis nostrud exercitation ullamco laboris nisi ut aliquip ex ea commodo consequat. Duis aute irure dolor in repreh enderit in voluptate velit esse cillum dolore eu fugiat nulla pariatur.</div>
<div class="btn btn-green" style="left:635px;top:2699px;width:112px;height:35px;font-size:13px;border-radius:5px">READ MORE</div>

<!-- stories -->
<div class="h2" style="top:2880px">PATIENT SUCCESS STORIES</div>
<div class="story" style="left:129px;top:2964px"><div class="ph" role="img" aria-label="Person with arms raised above a city at sunset" style="background:linear-gradient(180deg,#d9a37a,#8a5f4a 60%,#2f2a2e)"></div><div class="body"><div class="q">&ldquo;</div><h3>LOREM IPSUM IS SIMPLY DUM<br>MY TEXT OF THE PRINTING</h3><p>Sed ut perspiciatis unde omnis iste natus error sit voluptatem accusantium dolo remque laudantium, totam rem aperiam, eaque ipsa quae ab illo inventore veritatis et quas.</p></div></div>
<div class="story" style="left:450px;top:2964px"><div class="ph" role="img" aria-label="Man celebrating against a golden sunset" style="background:linear-gradient(180deg,#e9a24a,#f3c267 45%,#7a4b22)"></div><div class="body"><div class="q">&ldquo;</div><h3>LOREM IPSUM IS SIMPLY DUM<br>MY TEXT OF THE PRINTING</h3><p>Sed ut perspiciatis unde omnis iste natus error sit voluptatem accusantium dolo remque laudantium, totam rem aperiam, eaque ipsa quae ab illo inventore veritatis et quas.</p></div></div>
<div class="story" style="left:768px;top:2964px"><div class="ph" role="img" aria-label="Smiling woman hiking outdoors with friends" style="background:linear-gradient(120deg,#3b4a5c,#c23b3b 45%,#6d7a5a)"></div><div class="body"><div class="q">&ldquo;</div><h3>LOREM IPSUM IS SIMPLY DUM<br>MY TEXT OF THE PRINTING</h3><p>Sed ut perspiciatis unde omnis iste natus error sit voluptatem accusantium dolo remque laudantium, totam rem aperiam, eaque ipsa quae ab illo inventore veritatis et quas.</p></div></div>

<!-- call to action -->
<div class="abs cta" role="img" aria-label="Blurred photo of a clinic exercise session"></div>
<div class="abs" style="left:0;top:3485px;width:1200px;text-align:center;font-family:'Manrope',sans-serif;font-weight:800;font-size:40px;color:#fff">TAKE THE NEXT STEP</div>
<div class="abs" style="left:0;top:3547px;width:1200px;text-align:center;font-size:20px;line-height:28px;color:#fff">Lorem ipsum dolor sit amet, consectetur adipi scing elit sed do<br>eiusmod tempor incididunt ut labore et dolore magna.</div>
<div class="btn btn-green" style="left:476px;top:3630px;width:248px;height:47px;font-size:15.5px">BOOK AN APPOINTMENT</div>

<!-- footer -->
<div class="abs footer"></div>
<div class="abs" style="left:180px;top:3790px;width:60px;height:60px;border-radius:50%;background:var(--teal)"></div>
<div class="brand" style="left:130px;top:3895px;font-size:32px">KESTROVA</div>

<div class="f-h" style="left:398px;top:3795px;color:#fff">MENU</div>
<div class="f-menu" style="left:398px;top:3830px">HOME<br>ABOUT US<br>SERVICES<br>PATIENTS<br>CONTACT US</div>

<div class="f-h" style="left:617px;top:3795px;color:#fff">CONTACT US</div>
<div class="f-row" style="left:615px;top:3833px"><div class="c"><svg width="12" height="12" viewBox="0 0 24 24" fill="var(--footer)"><path d="M12 2a7 7 0 0 0-7 7c0 5 7 13 7 13s7-8 7-13a7 7 0 0 0-7-7zm0 9.5a2.5 2.5 0 1 1 0-5 2.5 2.5 0 0 1 0 5z"/></svg></div><div>2207 Larkspur Road<br>Alder Bay, CA 90412</div></div>
<div class="f-row" style="left:615px;top:3883px"><div class="c"><svg width="12" height="12" viewBox="0 0 24 24" fill="var(--footer)"><path d="M5 3h4l2 5-2.5 1.5a11 11 0 0 0 6 6L16 13l5 2v4a2 2 0 0 1-2 2A17 17 0 0 1 3 5a2 2 0 0 1 2-2z"/></svg></div><div>Call Us<br>555.014.2290</div></div>
<div class="f-row" style="left:615px;top:3933px"><div class="c"><svg width="12" height="12" viewBox="0 0 24 24" fill="var(--footer)"><path d="M3 5h18v14H3z M3 5l9 7 9-7" stroke="#fff" stroke-width="1.5"/></svg></div><div>E mail Us<br>info@kestrovapt.com</div></div>

<div class="f-h" style="left:958px;top:3795px;color:#fff">FOLLOW US</div>
<div class="f-row" style="left:958px;top:3833px"><div class="c"></div><div>Like us on<br>PEERLINE</div></div>
<div class="f-row" style="left:958px;top:3883px"><div class="c"></div><div>Follow us on<br>CHIRPNET</div></div>
<div class="f-row" style="left:958px;top:3933px"><div class="c"></div><div>Follow us on<br>WORKLINK</div></div>

<div class="abs" style="left:0;top:4053px;width:1200px;text-align:center;font-size:10.5px;color:#cfcfcf">Copyright &copy; 2021 All Rights Reserved</div>

</body>
</html>
```